Client Publishing Agency Brochure

We need a company brochure for a new company based in Cape Town, South Africa called Willowmere Lantern Studio (WLS).

We need a brochure marketing our publishing agency (wls:scribe) and our creative, interactive & print production division (wls:forge). Develop a fresh design concept which will direct the design of our new website in the near future. (So don't pay attention to our current web page. It does not reflect our brand).

wls:scribe is a content marketing agency offering our clients (B2B, B2C, NPO, Professional & Membership Organizations) branded publishing to build trust, authority and relationships with their customers. A typical content strategy may include communication through client print or online magazine, newsletters, microsite, website, social technology and plenty more). We want to communicate that company's need to change their mind set from promoting their products and begin to invest in developing a relationship with their potential & existing customers. The drive is a Return On Objectives (business & marketing objectives) and interest is a Return On Investment (ROI).

wls:forge is a creative, interactive & print production agency which supports our client's marketing collateral needs.
Updates

Hi Designers,

This is a response to questions posted earlier to assist you in your project.

Q.What will the size of brochure be?
A. A4 size with folder flap for the back cover

Q.Will it be a three panels double sided?
A. Depends on your creative concept. But if you make a 3 panel dbl side then layout two version for print (double sided 3 panel) and digital pdf (single pdf pages in sequence).

Q.The images that you supplied I know are just samples, What type of images are 
required? 
A. Depends on your creative concept. Let the style of the logo inspire you. What I liked in the examples is the classic, premium, quality feel. So no business stock imagery. I'm also a creative agency so that message needs to come through. Illustrated styles are welcome.

Q.Should design have same feel as your website? 
A. No. Our website is pending the outcome of the brochure. The brochure will be our creative direction for our new website. So creative an inspiring and clean brochure.

Please feel free to post additional questions. Good Luck and thank you for your participation.

Reason: The designers have not produced a style and concept that reflects our brand. Would like to guide them more to reach the right look for our company.

Hi Designers...

I have not been happy with the quality of ideas and execution of those ideas. This I understand could a combination of a poor brief and a non-guarenteed project.

I have rectified the brief and have guaranteed the award. Please don't hold back on your creativity and return the guarantee for high quality.

Please ask me any questions to better understand what we are looking for.

Remember. This brochure is a new design concept. Do not visit the web page for inspiration. The new design concept for the brochure will set the tone and inspire a new website.

Lets create a beautiful product together.

Thank you for your participation.

Reason: Designers are not following the brief, and not respecting the logo and colour policies/guidelines and those who are submitting work are not asking questions throughout the process to get a better understanding of what we need. All design submissions are always at the last minute. And some designers are are not real designers and using web development software to produce print designs. More importantly after taking time to advise designers of changes, no effort is made by designers to make changes. Each designer submits 1 idea and think that they are going to win the lottery. Where is the work ethic and quality of service? Where are the submissions from the designers who accepted the participation fee? There were a few designers who promised participation and never showed up. Maybe it all our fault? But we not happy with the service and level of creativity. Not sure if these designers are taking pride in their work or not. I know a few of you are.

Target Market(s)

B2B, B2C, NPO, Professional & Membership Organizations - Make up professionals and decision makers across sectors from Shipping and Logistics, Manufacturing, Legal to Art & Culture.

Industry/Entity Type

Communication

Requirements
Must have
• Size: A4
x 2 Panels
+ Folder flap (for A4 Paper, business card slot)
Styled map to our premises. See map attachment for example.

Pages: 10 including cover (if you need more than this let your design motivate the need for more pages)

(See logo use eps file)
(See colour use eps file)

Nice to have
• Styled map to our premises. See attachment for example.
Should not have
• Do not take any inspiration from our website. It is just a free template to show customers that it is still under construction.

Do not include stock symbols and typical business stock images. Remember we are a creative offering, so our brochure should show originality, innovation and individuality.

```html
<!DOCTYPE html>
<html lang="en">
<head>
<meta charset="utf-8">
<title>Willowmere Lantern Studio: Brochure Spread</title>
<link rel="stylesheet" href="https://fonts.googleapis.com/css2?family=Roboto+Condensed:wght@700&family=Roboto:wght@300;400&family=Tinos&display=swap">
<style>
  :root{
    --stage:#d9d9d9;
    --paper:#ffffff;
    --ink:#2a2a2a;
    --cyan:#1aa3e0;
    --magenta:#e0157f;
    --yellow:#ffe600;
    --red:#d0112b;
    --green:#3c9a35;
    --lavender:#9a85ad;
    --orange:#f4a21b;
    --lime:#8cbf2f;
    --blue:#1b7fd6;
    --sun-light:#fffbd0;
    --sun:#f3ee5a;
    --sun-deep:#c9b628;
  }
  *{box-sizing:border-box;margin:0;padding:0}
  html,body{width:1200px;height:900px;overflow:hidden;background:var(--stage)}
  body{position:relative;font-family:"Roboto",Arial,sans-serif;color:var(--ink)}

  .brochure{position:absolute;left:60px;top:60px;width:1080px;height:780px;display:flex;box-shadow:0 10px 30px rgba(0,0,0,.18)}

  .page{position:relative;height:100%;overflow:hidden}
  .page--left{width:430px;background:var(--paper)}
  .page--middle{width:430px}
  .page--flap{width:220px;background:var(--paper);border-left:1px solid #e6e6e6}

  .sunburst{position:absolute;background:
      radial-gradient(circle at 55% 40%, var(--sun-light) 0%, var(--sun) 45%, var(--sun-deep) 100%)}
  .page--left .sunburst{left:0;top:0;width:70px;height:100%}
  .page--middle .sunburst{inset:0}
  .margin-rule{position:absolute;left:78px;top:0;width:2px;height:100%;background:var(--magenta)}

  .tile-row{position:absolute;top:14px;display:flex;gap:6px}
  .page--left .tile-row{left:10px}
  .page--middle .tile-row{left:-10px}
  .tile{width:42px;height:42px;border-radius:9px;flex:none}
  .c-cyan{background:var(--cyan)}.c-magenta{background:var(--magenta)}.c-yellow{background:var(--yellow)}
  .c-red{background:var(--red)}.c-green{background:var(--green)}.c-lavender{background:var(--lavender)}
  .c-orange{background:var(--orange)}.c-lime{background:var(--lime)}.c-blue{background:var(--blue)}

  .column{position:absolute;top:88px;bottom:24px}
  .column--intro{left:92px;width:150px}
  .column--detail{left:258px;width:158px}
  .heading{font-family:"Roboto Condensed","Arial Narrow",sans-serif;font-weight:700;font-size:12.5px;line-height:1.25;text-transform:uppercase;margin-bottom:10px}
  .heading--red{color:var(--red)}
  .heading--green{color:var(--green)}
  .heading--blue{color:var(--cyan)}
  .body-sans{font-family:"Roboto",Arial,sans-serif;font-weight:300;font-size:9.6px;line-height:1.42;margin-bottom:9px}
  .body-serif{font-family:"Tinos","Times New Roman",serif;font-size:9.6px;line-height:1.35;margin-bottom:8px}

  .tab-stack{position:absolute;left:0;top:120px;display:flex;flex-direction:column;gap:12px}
  .tab{width:66px;height:82px;border-radius:0 12px 12px 0}
  .text-panel{position:absolute;left:82px;top:100px;width:170px;height:545px;background:rgba(255,255,255,.72);padding:8px 10px}
  .text-panel .body-serif{font-size:9.4px}

  .brand{position:absolute;left:20px;top:60px;width:180px;display:flex;flex-direction:column;align-items:center;gap:14px}
  .brand-dot{width:120px;height:120px;border-radius:50%;background:var(--ink)}
  .brand-name{font-family:"Roboto Condensed","Arial Narrow",sans-serif;font-weight:700;font-size:17px;line-height:1.2;text-align:center;color:var(--ink);text-transform:uppercase}
  .flap-copy{position:absolute;left:48px;top:310px;width:150px}
  .flap-copy .body-sans{font-size:9.2px}
  .flap-rule{position:absolute;left:0;top:588px;width:100%;height:2px;background:var(--cyan)}
  .tile-grid{position:absolute;left:0;top:598px;display:grid;grid-template-columns:repeat(5,40px);gap:4px 4px}
  .tile-grid .tile{width:40px;height:38px;border-radius:8px}
  .card-slot{position:absolute;left:28px;top:612px;width:150px;height:120px;background:var(--paper);border-radius:14px;box-shadow:0 2px 8px rgba(0,0,0,.25)}
</style>
</head>
<body>
<main class="brochure">

  <section class="page page--left">
    <div class="sunburst" role="img" aria-label="Abstract yellow light-burst photograph"></div>
    <div class="margin-rule"></div>
    <div class="tile-row">
      <span class="tile c-cyan"></span><span class="tile c-magenta"></span><span class="tile c-yellow"></span>
      <span class="tile c-red"></span><span class="tile c-green"></span><span class="tile c-lavender"></span>
      <span class="tile c-orange"></span><span class="tile c-green"></span><span class="tile c-cyan"></span>
    </div>

    <article class="column column--intro">
      <h2 class="heading heading--red">Stop promoting products. Start building relationships that last.</h2>
      <p class="body-sans">Willowmere Lantern Studio is a Cape Town content house built on one belief: customers stay with the brands they trust. We help companies earn that trust through stories worth reading.</p>
      <p class="body-sans">wls:scribe is our publishing agency. We plan, write and publish branded content for B2B, B2C, NPO, professional and membership organisations, from shipping and logistics to legal, manufacturing, art and culture.</p>
      <p class="body-sans">Your content strategy may include a print or online magazine, newsletters, a microsite, a website, social technology and much more. Every channel speaks with one clear voice, shaped around the people you want to reach.</p>
      <p class="body-sans">The shift we ask of our clients is simple but bold: move from selling at customers to investing in a relationship with them. Authority grows when you share knowledge, answer real questions and show up consistently, issue after issue.</p>
      <p class="body-sans">We measure that drive as a Return On Objectives.</p>
      <p class="body-sans">Your business and marketing goals set the course.</p>
    </article>

    <article class="column column--detail">
      <h2 class="heading heading--green">wls:scribe: branded publishing that builds trust and authority.</h2>
      <p class="body-serif">Every engagement starts with listening. We learn who your customers are, what they need to know and where they spend their time, then map a content plan that serves them before it sells to them.</p>
      <p class="body-serif">Our editors, writers and designers produce magazines, newsletters and digital features with the care of a consumer title. The result is publishing your audience looks forward to, not marketing it learns to ignore.</p>
      <p class="body-serif">Across print and screen we keep your voice consistent. A quarterly magazine can feed a newsletter, a microsite and social posts, so each story works harder and reaches further for the same investment.</p>
      <p class="body-serif">Relationships, not reach, are the goal.</p>
      <p class="body-serif">We report on what matters: readership, engagement and progress against the business and marketing objectives you set with us.</p>
      <p class="body-serif">Interest is the Return On Investment. Objectives are the drive.</p>
    </article>
  </section>

  <section class="page page--middle">
    <div class="sunburst" role="img" aria-label="Abstract yellow light-burst photograph filling the page"></div>
    <div class="tile-row">
      <span class="tile c-magenta"></span><span class="tile c-red"></span><span class="tile c-yellow"></span>
      <span class="tile c-orange"></span><span class="tile c-magenta"></span><span class="tile c-lime"></span>
      <span class="tile c-blue"></span>
    </div>
    <div class="tab-stack">
      <span class="tab c-blue"></span><span class="tab c-lavender"></span><span class="tab c-lime"></span>
      <span class="tab c-red"></span><span class="tab c-magenta"></span>
    </div>
    <article class="text-panel">
      <h2 class="heading heading--green">wls:forge: creative, interactive and print production.</h2>
      <p class="body-serif">wls:forge is our creative, interactive and print production division. It supports your marketing collateral needs from the first sketch to the final press sheet or published page.</p>
      <p class="body-serif">Brochures, folders, annual reports, packaging, websites, interactive PDFs and campaign material are designed and produced in one studio, so ideas travel intact.</p>
      <p class="body-serif">One team, one standard of craft.</p>
      <p class="body-serif">We manage print buying, proofing and quality checks, and build digital pieces that load fast and read well on any screen.</p>
      <p class="body-serif">Fresh concepts, no stock clichés. Original work made for your brand.</p>
      <p class="body-serif">Bring us a brief, a deadline or just an idea, and we will shape it into collateral you are proud to hand over.</p>
    </article>
  </section>

  <aside class="page page--flap">
    <div class="brand">
      <span class="brand-dot"></span>
      <p class="brand-name">Willowmere Lantern Studio</p>
    </div>
    <div class="flap-copy">
      <h2 class="heading heading--blue">Let's create something beautiful together.</h2>
      <p class="body-sans">Visit our Cape Town studio to talk about your audience, your objectives and the stories only your organisation can tell. We will show you how publishing and production work together to build lasting customer relationships.</p>
      <p class="body-sans">Tuck your card in the slot below and we will be in touch to plan your first issue.</p>
    </div>
    <div class="flap-rule"></div>
    <div class="tile-grid">
      <span class="tile c-red"></span><span class="tile c-green"></span><span class="tile c-lavender"></span><span class="tile c-magenta"></span><span class="tile c-green"></span>
      <span class="tile c-cyan"></span><span class="tile c-blue"></span><span class="tile c-magenta"></span><span class="tile c-orange"></span><span class="tile c-lime"></span>
      <span class="tile c-yellow"></span><span class="tile c-red"></span><span class="tile c-cyan"></span><span class="tile c-lavender"></span><span class="tile c-magenta"></span>
    </div>
    <div class="card-slot"></div>
  </aside>

</main>
</body>
</html>
```